TalkNest Needs a Brochure Design

We need a brochure (sent as an e-mail message and via mail), to market our professional development seminars. We provide seminars related to autism and non-verbal communication. Brochure should have certain information (see Must Have Priorities) and be designed for target market.

Please submit only 2-3 of your best designs.
Updates

I have added a word file with detail information about the seminar. We want a design that can be sent both as e-mail and regular mail. A 8 x 10 design that can be folded and mailed will meet our requirements. We are hoping that we will be able to send the one page as an e-mail and the back can be used for advertisement.

Target Market(s)

Physicians, Speech-Language Pathologists, Occupational Therapist, Early Intervention Specialists, Special Educators.

Industry/Entity Type

Communication

Font styles to use
Sans Serif

Colors
3176b5
33b7a4
f68d4d

Requirements
Must have
• See the attached file. In addition the brochure must have:
1 Logo for academic accreditation and CEU information.
2. Registration Fees and how to register.
Nice to have
• Photographs.

```html
<!DOCTYPE html>
<html lang="en">
<head>
<meta charset="utf-8">
<title>TalkNest Seminar Brochure</title>
<link rel="stylesheet" href="https://fonts.googleapis.com/css2?family=Archivo+Black&family=Open+Sans:wght@400;600;700&display=swap">
<style>
:root{
  --blue:#3176b5;
  --navy:#1d4f8c;
  --teal:#1f8f84;
  --teal-light:#33b7a4;
  --green:#3a9a3a;
  --orange:#f68d4d;
  --ink:#1b1b1b;
  --stage:#2a2a2a;
  --white:#ffffff;
}
*{margin:0;padding:0;box-sizing:border-box}
html,body{width:1200px;height:791px;overflow:hidden;background:var(--stage);font-family:"Open Sans",Arial,sans-serif;color:var(--ink)}
.canvas{position:relative;width:1200px;height:791px}
.page{position:absolute;overflow:hidden}
.flyer{left:32px;top:36px;width:558px;height:721px;background:linear-gradient(180deg,#d9eefb 0%,#a9d6f3 45%,#c9e6f8 100%)}
.postcard{left:618px;top:36px;width:557px;height:716px;background:linear-gradient(180deg,#ffffff 55%,#d8eef9 100%)}
.abs{position:absolute}

.logo{display:flex;align-items:center;gap:8px}
.logo-mark{width:22px;height:22px;background:var(--blue)}
.logo-name{font-family:"Open Sans",sans-serif;font-weight:600;color:var(--blue)}

.flyer .logo-box{left:13px;top:14px;width:175px;height:68px;background:var(--white);padding:0 16px}
.flyer .logo-name{font-size:22px}

.title-band{left:220px;top:0;width:338px;height:150px}
.title{font-family:"Archivo Black",Impact,sans-serif;text-align:center;line-height:1}
.title .t1{left:226px;top:15px;width:320px;color:var(--green);font-size:23px}
.title .t1 small{font-size:15px}
.title .t2{left:226px;top:44px;width:320px;color:var(--green);font-size:17.5px}
.title .t3{left:245px;top:62px;width:280px;color:var(--navy);font-size:58px;letter-spacing:1px}
.title .t4{left:290px;top:127px;width:260px;color:var(--green);font-size:17.5px}

.spine{left:34px;top:118px;width:10px;height:312px;background:var(--navy);border-radius:5px}
.intro{left:15px;top:120px;width:258px;height:89px;background:var(--orange);color:var(--white);font-size:7.4px;line-height:1.3;padding:6px 8px;text-align:justify}
.arrow-bar{left:0;top:219px;width:270px;height:16px}
.outcomes{left:15px;top:247px;width:290px;height:165px;background:var(--teal);color:var(--white);font-size:7.8px;line-height:1.35;padding:6px 8px}
.outcomes ul{list-style:none;margin-top:4px}
.outcomes li{position:relative;padding-left:13px;margin-bottom:3px}
.outcomes li::before{content:"";position:absolute;left:2px;top:4px;width:5px;height:5px;border-radius:50%;background:var(--white)}

.event-date{left:305px;top:174px;width:250px;text-align:center;font-weight:700;color:var(--navy);font-size:22px}
.venue{left:300px;top:208px;width:260px;text-align:center;font-weight:700;color:var(--navy);font-size:16px;line-height:1.25}

.tablet{background:#1a1a1a;border-radius:8px;padding:9px}
.tablet .screen{width:100%;height:100%}
.tablet-a{left:323px;top:262px;width:153px;height:104px}
.tablet-b{left:385px;top:352px;width:153px;height:90px}

.schedule{left:22px;top:442px;width:275px;border-collapse:collapse;font-size:7.4px}
.schedule th{background:var(--navy);color:var(--white);text-align:left;font-size:11px;font-weight:700;padding:2px 6px;height:17px}
.schedule td{padding:2px 4px;border-bottom:1px solid rgba(255,255,255,.7);vertical-align:middle;line-height:1.2}
.schedule td:first-child{width:56px;font-weight:600}

.speaker-label{left:310px;top:482px;font-size:11px;line-height:1}
.speaker-name{left:310px;top:493px;font-size:16px;font-weight:700;line-height:1}
.speaker-name small{font-size:8px;font-weight:400}
.bio-box{left:308px;top:507px;width:240px;height:118px;background:var(--orange)}
.bio-text{left:312px;top:511px;width:142px;color:var(--white);font-size:6.2px;line-height:1.2;text-align:justify}
.bio-photo{left:456px;top:516px;width:87px;height:104px}

.register{left:366px;top:647px;width:192px;height:28px;background:var(--green);color:var(--white);font-weight:700;font-size:9.5px;padding:2px 8px;text-align:right;line-height:1.25}
.more-info{left:356px;top:675px;width:202px;height:36px;background:var(--navy);color:var(--white);font-weight:700;font-size:9.5px;text-align:center;padding:4px 4px;line-height:1.45}
.badge{left:22px;top:672px;width:80px;height:40px;background:var(--white);border:1px solid #888;padding:2px;display:flex;gap:3px}
.badge-shape{width:12px;height:12px;background:#444;flex:none}
.badge-text{font-size:3.4px;line-height:1.2;color:#333}

.pc-band-top{left:0;top:0;width:557px;height:59px;background:linear-gradient(180deg,#2f7fc0,#5aa3d8)}
.pc-head{left:0;top:14px;width:557px;text-align:center;color:var(--white);font-size:21px;font-weight:600}
.pc-photo{left:0;top:59px;width:557px;height:305px;background:linear-gradient(180deg,#7fb8e6 0%,#b5d7ee 40%,#7aa06a 60%,#5d8fb5 100%)}
.pc-band{left:0;top:267px;width:557px;height:97px;background:rgba(40,110,175,.82);color:var(--white);text-align:center;font-weight:600;font-size:19.5px;line-height:1.3;padding-top:7px}
.postcard .logo-pc{left:44px;top:386px}
.postcard .logo-name{font-size:23px}
.postcard .logo-mark{width:26px;height:26px}
.tagline{left:40px;top:461px;font-size:10px;font-weight:600;color:#333}
.stamp{left:415px;top:392px;width:124px;height:112px;border:1px solid #777}
.address-line{left:139px;width:296px;height:1px;background:#999}
</style>
</head>
<body>
<main class="canvas">

  <section class="page flyer" aria-label="Seminar flyer">
    <svg class="abs title-band" viewBox="0 0 338 150" aria-hidden="true">
      <path d="M40 0 H338 V150 C260 120 150 95 60 105 Z" fill="#1f8f84" opacity=".85"/>
      <path d="M0 0 H60 C110 40 230 60 338 40 V0 Z" fill="#33b7a4" opacity=".35"/>
    </svg>

    <div class="abs logo-box logo"><span class="logo-mark"></span><span class="logo-name">TalkNest</span></div>

    <div class="title">
      <div class="abs t1">MOBILE TECHNOLOGY <small>TO</small></div>
      <div class="abs t2">SUPPORT COMMUNICATION IN</div>
      <div class="abs t3">AUTISM</div>
      <div class="abs t4">SPECTRUM DISORDERS</div>
    </div>

    <div class="abs spine"></div>
    <p class="abs intro">With the current availability of mobile technology (e.g., Pearl Pad, Orbit OS) individuals with autism have many options available for communication. This course focused on visual support, accessibility, and language learning through mobile technology. Compared specialized AAC “apps” and assessed contemporary evidence for effective use of mobile technology by children with autism to enhance their communication skills.</p>

    <svg class="abs arrow-bar" viewBox="0 0 270 16" aria-hidden="true">
      <path d="M0 5 H240 L270 8 L240 11 H0 Z" fill="#1d4f8c"/>
    </svg>

    <div class="abs outcomes">
      <p>Learner's Outcomes:<br>As a result of this seminar, the participant will be able to:</p>
      <ul>
        <li>Summarize issues related to information processing, visual attention, and visual support in children with autism</li>
        <li>Decide about accessibility of mobile technology by children with autism</li>
        <li>Integrate language learning strategies using mobile technology in children with autism</li>
        <li>Compare contemporary specialized AAC “apps” for children with autism</li>
        <li>Assess contemporary evidence for effectiveness of mobile technology by children with autism</li>
      </ul>
    </div>

    <div class="abs event-date">September 19, 2014</div>
    <div class="abs venue">220 Harbor Avenue<br>Chicago, Il 60601</div>

    <div class="abs tablet tablet-a"><div class="screen" role="img" aria-label="Photo of a girl holding puzzle pieces" style="background:linear-gradient(135deg,#e9d9a8,#cfc7b8)"></div></div>
    <div class="abs tablet tablet-b"><div class="screen" role="img" aria-label="Photo of a child sitting on grass under a blue sky" style="background:linear-gradient(180deg,#5aa8e6 0%,#8cc6f0 60%,#5c9a3a 62%,#4d8a30 100%)"></div></div>

    <table class="abs schedule">
      <thead><tr><th>Time</th><th>Topic</th></tr></thead>
      <tbody>
        <tr><td>8:30 – 9:00</td><td>Registration and Coffee</td></tr>
        <tr><td>9:00 – 10:00</td><td>Information Processing, visual attention, and visual support in children with autism</td></tr>
        <tr><td>10:00 – 10:45</td><td>Accessibility issues related to use of mobile technology</td></tr>
        <tr><td>10:45 – 11:00</td><td>Break</td></tr>
        <tr><td>11:00 – 12:00</td><td>Language learning strategies using mobile technology</td></tr>
        <tr><td>12:00 – 12:30</td><td>Lunch</td></tr>
        <tr><td>12:30 – 13:00</td><td>Video presentations</td></tr>
        <tr><td>13:00 – 13:45</td><td>Contemporary specialized AAC apps for children with autism</td></tr>
        <tr><td>13:45 – 14:00</td><td>Break</td></tr>
        <tr><td>14:00 – 14:30</td><td>Assessment of contemporary evidence for effectiveness of mobile technology</td></tr>
        <tr><td>14:30 – 15:00</td><td>Wrap up discussion, questions, and comments</td></tr>
      </tbody>
    </table>

    <div class="abs speaker-label">Speaker:</div>
    <div class="abs speaker-name">Arun Mehta<small>, Ph.D., CCC-SLP</small></div>
    <div class="abs bio-box"></div>
    <p class="abs bio-text">Arun Mehta is an Associate Professor of Communication Disorders at Lakeshore State University. He earned his doctorate from Midwest Valley University. He has working experience in diverse settings including private practice, hospitals, long term residential settings and integrated school settings. His areas of research interest are: assistive technology, early language intervention, and reading disabilities. He has over 30 publications and over 100 presentations at national and international scientific meetings. He is a consulting editor for Augmentative and Alternative Communication.</p>
    <div class="abs bio-photo" role="img" aria-label="Portrait photo of the speaker" style="background:linear-gradient(180deg,#9cc48a,#6f8f5e)"></div>

    <div class="abs badge">
      <span class="badge-shape"></span>
      <p class="badge-text">Lakeshore State University is approved by the Continuing Education Board to offer courses. This course is offered for 0.6 CEUs intermediate level professional area.</p>
    </div>

    <div class="abs register">Register by:&nbsp; August 31, 2014<br>Registration Fees:&nbsp; $100</div>
    <div class="abs more-info">For more information, please visit<br>www.arunmehtaseminars.com</div>
  </section>

  <section class="page postcard" aria-label="Mailing postcard">
    <div class="abs pc-band-top"></div>
    <div class="abs pc-head">Earn CEUs with exciting view of Lake Michigan</div>
    <div class="abs pc-photo" role="img" aria-label="Photo of the Chicago skyline with boats in a harbour"></div>
    <div class="abs pc-band">Mobile Technology to Support Communication in<br>Individuals with Autism Spectrum Disorders<br>Friday, September 19, 2014</div>

    <div class="abs logo logo-pc"><span class="logo-mark"></span><span class="logo-name">TalkNest</span></div>
    <div class="abs tagline">Helping Children Earlier to Succeed Latter</div>
    <div class="abs stamp"></div>
    <div class="abs address-line" style="top:565px"></div>
    <div class="abs address-line" style="top:600px"></div>
    <div class="abs address-line" style="top:635px"></div>
  </section>

</main>
</body>
</html>
```